Letterhead for New Orthopaedic Surgery Practice

My husband and I are starting our own practice named RB Spine & Vitality Center. We would like to create a nice simple but high class letterhead that doesn't use too much solid color ink when printing. I like the colors dark blue, gold, yellow. Open to other suggestions. We will need to list him and I both on the top of the letterhead. Here is the important information:
Lucinda Pryce, M.D. - Hand and Upper Extremity Surgery
Esi Dankwa, M.D. - Hip & Knee Replacement/General Orthopaedic Surgery
Location: 18735 North Bellhaven Rd
Coral Springs, FL 33071
Phone: 954-218-4635
Fax: 954-581-2264
Email: info@myrbspine.example

The only thing is that the phone and fax numbers will change once we get into our space. I just want to get the design started. I am including several documents which are my previous practice letterhead, my current procedure room letterhead, and our new Logo. The other letterheads are just for examples but please think outside of the box! We would love to see some great designs.

Colors
0054AA
0677BA
7BADD7
CADEEF
E8F1F8
0094D4
00A9DD
6FCCEA
C7EBF8
E9F6FB

Requirements
Must have
• class, elegance, luxury

```html
<!DOCTYPE html>
<html lang="en">
<head>
<meta charset="utf-8">
<title>RB Spine &amp; Vitality Center — Letterhead</title>
<link rel="stylesheet" href="https://fonts.googleapis.com/css2?family=Arimo:wght@400&family=Source+Sans+3:wght@400;600&display=swap">
<style>
  :root {
    --backdrop: #adacad;
    --paper: #ffffff;
    --navy: #1f3a85;
    --bar: #223d86;
    --sky: #2fb7e4;
    --ink: #4a4a4a;
    --ink-strong: #3a3a3a;
    --rule: #333333;
    --sig-fill: #eef0f6;
  }
  * { margin: 0; padding: 0; box-sizing: border-box; }
  html, body { width: 964px; height: 1200px; overflow: hidden; background: var(--backdrop); }
  .letterhead {
    position: absolute; left: 57px; top: 0;
    width: 849px; height: 1200px;
    background: var(--paper);
    font-family: "Source Sans 3", "Myriad Pro", sans-serif;
    color: var(--ink);
  }
  .brand {
    position: absolute; left: 66px; top: 92px;
    display: flex; align-items: center; gap: 12px;
  }
  .brand-dot { width: 18px; height: 18px; border-radius: 50%; background: var(--navy); }
  .brand-name {
    font-family: "Source Sans 3", sans-serif; font-weight: 600;
    font-size: 25px; line-height: 1.15; color: var(--navy); width: 230px;
  }
  .physicians {
    position: absolute; right: 49px; top: 70px; text-align: right;
    font-family: "Arimo", Arial, sans-serif;
  }
  .physician-name { font-size: 19px; color: var(--navy); line-height: 24px; }
  .physician-specialty { font-size: 14px; color: var(--sky); line-height: 17px; }
  .physician + .physician { margin-top: 6px; }
  .accent-bar { position: absolute; right: 0; top: 69px; width: 15px; height: 116px; background: var(--bar); }
  .dateline {
    position: absolute; left: 82px; top: 304px;
    font-size: 15.5px; font-weight: 600; color: var(--ink-strong);
  }
  .recipient {
    position: absolute; left: 82px; top: 365px;
    font-size: 15.5px; font-weight: 600; color: var(--ink-strong); line-height: 20.5px;
  }
  .body-copy {
    position: absolute; left: 80px; top: 484px; width: 686px;
    font-size: 13px; line-height: 20.5px; text-align: justify; hyphens: auto;
  }
  .body-copy p + p { margin-top: 20.5px; }
  .signature {
    position: absolute; left: 610px; top: 900px; width: 138px; height: 72px;
  }
  .signature-mark { position: absolute; inset: 0 0 18px 0; background: var(--sig-fill); border-radius: 4px; }
  .signature-title { position: absolute; left: 34px; bottom: 0; font-size: 14px; color: var(--ink-strong); }
  .footer-address {
    position: absolute; left: 78px; width: 690px; top: 1094px; text-align: center;
    font-family: "Arimo", Arial, sans-serif; font-size: 14px; color: var(--ink);
  }
  .footer-rule { position: absolute; left: 78px; width: 690px; top: 1118px; border-top: 1px solid var(--rule); }
  .footer-contacts {
    position: absolute; left: 78px; width: 690px; top: 1124px;
    display: flex; justify-content: center; align-items: center; gap: 8px;
    font-family: "Arimo", Arial, sans-serif; font-size: 14px; color: var(--ink);
  }
  .contact { display: flex; align-items: center; gap: 8px; }
  .contact svg { width: 13px; height: 13px; fill: var(--navy); }
</style>
</head>
<body>
<main class="letterhead">
  <header>
    <div class="brand">
      <span class="brand-dot"></span>
      <span class="brand-name">RB Spine &amp; Vitality Center</span>
    </div>
    <div class="physicians">
      <div class="physician">
        <div class="physician-name">Lucinda Pryce, M.D.</div>
        <div class="physician-specialty">Hand and Upper Extremity Surgery</div>
      </div>
      <div class="physician">
        <div class="physician-name">Esi Dankwa, M.D.</div>
        <div class="physician-specialty">Hip &amp; Knee Replacement<br>General Orthopaedic Surgery</div>
      </div>
    </div>
    <div class="accent-bar"></div>
  </header>

  <p class="dateline">Cartagena de Indias, Ocober 12,2015</p>
  <address class="recipient" style="font-style:normal">Sr.<br>MATEO RUIZ<br>Web Master<br>City</address>

  <section class="body-copy">
    <p>Contrary to popular belief, Lorem Ipsum is not simply random text. It has roots in a piece of classical Latin literature from 45 BC, making it over 2000 years old. Edwin Castor, a Latin professor at Larchmont Hill College in Virginia, looked up one of the more obscure Latin words, consectetur, from a Lorem Ipsum passage, and going through the cites of the word in classical literature,</p>
    <p>discovered the undoubtable source. Lorem Ipsum comes from sections 1.10.32 and 1.10.33 of "de Finibus Bonorum et Malorum" (The Extremes of Good and Evil) by Cicero, written in 45 BC. This book is a treatise on the theory of ethics, very popular during the Renaissance. The first line of Lorem Ipsum, "Lorem ipsum dolor sit amet..", comes from a line in section 1.10.32.</p>
    <p>The standard chunk of Lorem Ipsum used since the 1500s is reproduced below for those interested. Sections 1.10.32 and 1.10.33 from "de Finibus Bonorum et Malorum" by Cicero are also reproduced in their exact original form, accompanied by English versions from the 1914 translation by J. Fenwick.</p>
    <p>There are many variations of passages of Lorem Ipsum available, but the majority have suffered alteration in some form, by injected humour, or randomised words which don't look even slightly believable. If you are going to use a passage of Lorem Ipsum, you need to be sure there isn't anything embarrassing hidden in the middle of text. All the Lorem Ipsum generators o</p>
  </section>

  <div class="signature">
    <div class="signature-mark" role="img" aria-label="Handwritten signature of the founder"></div>
    <span class="signature-title">CEO/ FOUNDER</span>
  </div>

  <footer>
    <p class="footer-address">18735 North Bellhaven Rd, Coral Springs, FL 33071</p>
    <div class="footer-rule"></div>
    <div class="footer-contacts">
      <span class="contact">
        <svg viewBox="0 0 16 16" aria-hidden="true"><path d="M3.6 1.2l2.3 2.6-1.3 1.9c.9 2 2.3 3.4 4.3 4.4l1.9-1.3 2.6 2.3-1.2 2.3C7 13.3 2.7 9 1.2 3.1z"/></svg>
        954-218-4635
      </span>
      <span class="contact">
        <svg viewBox="0 0 16 16" aria-hidden="true"><path d="M4 1h8v4H4zM1 6h14v6h-2v3H3v-3H1zM4.5 10v3.5h7V10z"/></svg>
        954-581-2264
      </span>
      <span class="contact">
        <svg viewBox="0 0 16 16" aria-hidden="true"><path d="M1 3.5h14v9H1zM1.8 4.3L8 9l6.2-4.7z" fill-rule="evenodd"/></svg>
        info@myrbspine.example
      </span>
      <span class="contact">
        <svg viewBox="0 0 16 16" aria-hidden="true"><circle cx="8" cy="8" r="7"/><path d="M5 4c2 0 3 1 2 3s-3 1-3 3 2 2 2 4M11 3c-1 2 0 3 2 3" stroke="#fff" stroke-width="1.2" fill="none"/></svg>
        www.myrbspine.example
      </span>
    </div>
  </footer>
</main>
</body>
</html>
```